Web Design Project

We need a web design for a new company. We have a logo, and we've identified the style of a website that we'd like to adapt (www.tovendrafield.example). We do not sell to the public. The purpose of the site is (1) to allow our appointed sales partners to log in to our proprietary database system and (2) to provide a basic web presence and some basic information about our company.

We sell business insurance through independent agents - our sales partners.

Please do not use a photo of a person/s as a central design element, or at all.

Target Market(s)

The purpose of the site is not to sell, but to provide a professional landing page for a log in and some basic company information.

Industry/Entity Type

Business

Requirements
Must have
• A professional look. Agent log in must be central, clear and easy. Use of our logo and our colors.
Should not have
• Photos of people

```html
<!DOCTYPE html>
<html lang="en">
<head>
<meta charset="utf-8">
<title>Larkmoor Insurance</title>
<link href="https://fonts.googleapis.com/css2?family=Source+Sans+3:ital,wght@0,400;0,600;1,400&family=Arimo:ital,wght@0,400;0,700;1,400&display=swap" rel="stylesheet">
<style>
  :root {
    --sky-top: #2f64a4;
    --sky-bottom: #4a82c2;
    --navy: #0b3650;
    --navy-deep: #052638;
    --footer: #06213a;
    --ink: #2b2b2b;
    --muted: #8a8f96;
    --link: #8696a6;
    --panel: #f1f1f1;
    --field-border: #d9d9d9;
    --rule: #d6d6d6;
    --white: #ffffff;
  }
  * { box-sizing: border-box; margin: 0; padding: 0; }
  html, body { width: 1200px; height: 980px; overflow: hidden; background: var(--white); }
  body { position: relative; font-family: "Arimo", Arial, sans-serif; color: var(--ink); }
  .abs { position: absolute; }

  .sky-band { left: 0; top: 0; width: 1200px; height: 350px;
    background: linear-gradient(180deg, var(--sky-top), var(--sky-bottom)); }

  .brand { left: 177px; top: 34px; display: flex; align-items: center; gap: 8px;
    font-family: "Source Sans 3", sans-serif; font-weight: 600; font-size: 17px; color: var(--white); }
  .brand-mark { width: 34px; height: 34px; background: var(--navy); border-radius: 4px; }

  .search-field { left: 799px; top: 23px; width: 169px; height: 23px; border-radius: 12px;
    background: var(--white); border: 1px solid #c9d6e5; font-size: 11px; color: #c3c3c3; padding: 4px 14px; }
  .search-go { left: 972px; top: 23px; width: 38px; height: 23px; border-radius: 12px;
    background: var(--navy); color: var(--white); font-size: 10px; font-weight: 700; text-align: center; line-height: 23px; }

  .main-nav { left: 482px; top: 56px; width: 541px; height: 49px; border-radius: 6px;
    background: linear-gradient(180deg, #0f4663, var(--navy-deep)); border: 1px solid #041b28;
    display: flex; align-items: center; justify-content: center;
    font-family: "Source Sans 3", sans-serif; font-size: 14px; color: var(--white); letter-spacing: .3px; }
  .main-nav span { padding: 0 14px; border-left: 1px solid #1c5270; line-height: 20px; }
  .main-nav span:first-child { border-left: none; }

  .hero { left: 177px; top: 122px; width: 846px; height: 333px; border: 3px solid #3e73b1;
    border-top: none; border-radius: 6px 6px 10px 10px; overflow: hidden; }
  .hero-fill { width: 100%; height: 100%;
    background: linear-gradient(100deg, #c9d3dc 0%, #8c8e92 30%, #dfe3e6 55%, #f3f3f2 80%, #dcdfe2 100%); }
  .slide-dots { left: 944px; top: 433px; display: flex; gap: 3px; }
  .slide-dots i { display: block; width: 14px; height: 14px; border-radius: 4px; background: var(--navy); }
  .slide-dots i.active { background: #3a6fae; }

  .section-title { font-family: "Source Sans 3", sans-serif; font-style: italic; font-size: 21px; color: #333; font-weight: 400; }
  .btn-dark { width: 68px; height: 24px; border-radius: 4px; background: linear-gradient(180deg, #555, #2d2d2d);
    color: var(--white); font-size: 9px; text-align: center; line-height: 24px; }

  /* Agent login, centred on the banner */
  .login-panel { left: 469px; top: 190px; width: 262px; height: 196px; border-radius: 8px;
    background: var(--panel); box-shadow: 0 4px 18px rgba(5, 38, 56, .25); padding: 8px 15px 0; }
  .login-panel .section-title { font-size: 22px; line-height: 28px; margin-left: -3px; }
  .login-panel .field { width: 211px; height: 23px; border-radius: 12px; background: var(--white);
    border: 1px solid var(--field-border); font-size: 11px; color: #c5c5c5; padding: 4px 14px; margin-top: 10px; }
  .login-panel .field:first-of-type { margin-top: 10px; }
  .login-panel .btn-dark { margin: 11px 0 0 13px; }
  .login-meta { margin: 10px 0 0 13px; width: 200px; font-size: 10.5px; line-height: 16px; color: #333; }
  .remember { display: flex; align-items: center; gap: 5px; }
  .remember i { display: block; width: 9px; height: 9px; background: var(--white); }
  .login-links { display: flex; justify-content: space-between; }

  .advice-title { left: 183px; top: 476px; }
  .advice-photo { left: 182px; top: 520px; width: 172px; height: 155px; border: 3px solid #cfd6dd;
    background: linear-gradient(120deg, #f1f1f1, #a6a8ac 55%, #e8e8e8); }
  .advice-lead { left: 375px; top: 531px; width: 330px; font-weight: 700; font-size: 11px; line-height: 15px; color: #222; }
  .advice-body { left: 375px; top: 578px; width: 330px; font-size: 10.7px; line-height: 15.3px; color: var(--muted); }
  .advice-btn { left: 376px; top: 652px; }
  .divider { left: 182px; top: 700px; width: 551px; height: 1px; background: var(--rule); }

  .testimonial-title { left: 182px; top: 728px; font-size: 22px; }
  .quote-mark { left: 182px; top: 772px; width: 60px; height: 48px; }
  .testimonial-body { left: 182px; top: 769px; width: 512px; font-style: italic; font-size: 10.6px; line-height: 15.3px; color: var(--muted); }
  .testimonial-name { left: 182px; top: 856px; font-weight: 700; font-size: 11px; color: #222; }

  .services-title { left: 761px; top: 476px; font-size: 22px; }
  .services-list { left: 761px; top: 508px; list-style: none; }
  .services-list li { display: flex; align-items: center; gap: 9px; height: 27px; font-size: 11px; color: var(--link); }
  .services-list li span { text-decoration: underline; text-decoration-color: #c4ccd4; text-underline-offset: 3px; }
  .bullet { width: 18px; height: 18px; border: 1px solid #d3d3d3; border-radius: 3px; background: #fafafa; }
  .services-btn { left: 760px; top: 652px; }

  .footer { left: 0; top: 904px; width: 1200px; height: 76px; background: var(--footer); }
  .footer-links { left: 182px; top: 923px; font-size: 10.5px; color: var(--white); }
  .footer-copy { left: 182px; top: 946px; font-size: 10.5px; color: var(--white); }
  .social { left: 905px; top: 934px; display: flex; gap: 8px; }
  .social i { display: block; width: 14px; height: 14px; border-radius: 2px; }
</style>
</head>
<body>
  <div class="abs sky-band"></div>

  <div class="abs brand"><span class="brand-mark"></span>Larkmoor Insurance</div>

  <div class="abs search-field">search</div>
  <div class="abs search-go">GO</div>

  <nav class="abs main-nav">
    <span>Home</span><span>About Us</span><span>Services</span><span>Investors</span><span>FAQ's</span><span>Blog</span><span>Contact Us</span>
  </nav>

  <div class="abs hero"><div class="hero-fill" role="img" aria-label="Banner image: bright office interior with a blurred business meeting"></div></div>
  <div class="abs slide-dots"><i class="active"></i><i></i><i></i><i></i></div>

  <section class="abs login-panel" aria-label="Member login">
    <h2 class="section-title">Member Login</h2>
    <div class="field">Username</div>
    <div class="field">Password</div>
    <div class="btn-dark">LOGIN</div>
    <div class="login-meta">
      <div class="remember"><i></i>Remeber me</div>
      <div class="login-links"><span>Forgot Password?</span><span>Register Now</span></div>
    </div>
  </section>

  <h2 class="abs section-title advice-title">Ask professionals for business advice!</h2>
  <div class="abs advice-photo" role="img" aria-label="Image: business adviser reviewing a document"></div>
  <p class="abs advice-lead">Morbi nunc odio gravida arsus nectus oremaecenas triique seuis ultricies pharetra magnnec malesuada</p>
  <p class="abs advice-body">Luctus et ultriceosue cubiliaisse sollicitudin velit sed le elit magna hendrerit sit amet, tincidunt ac viverra sed, nullec porta diaeumet consectetuer adipiscisent vestibulum molestie Inean nonummy hendrerit mauris. Phasellus porta.</p>
  <div class="abs btn-dark advice-btn">READ MORE</div>
  <div class="abs divider"></div>

  <h2 class="abs section-title testimonial-title">Testimonial</h2>
  <svg class="abs quote-mark" viewBox="0 0 60 48" aria-hidden="true">
    <path d="M4 40 Q4 14 24 6 L26 10 Q14 18 16 26 L24 26 L24 40 Z M32 40 Q32 14 52 6 L54 10 Q42 18 44 26 L52 26 L52 40 Z" fill="#f1f1f1"/>
  </svg>
  <p class="abs testimonial-body">Etiam cursus leo vel metuulla facilienean nec erosstibulum ante ipsum primis in faucibusluctus et ultrices pouuere cubiliaisse sollicitudin velit sed le elit magna, hendrerit sit amncidunt ac viverra sed, nullec porta diam eu massaisque diam lorem, interdum vitae, dapibus ac, scelerisque vitae, peonec eget tellus non erat lacinia fermentuonec in lum iaculis lacinia est. Proin dictum elementum velusce euismod consequat antem ipsum dolor sit amet.</p>
  <p class="abs testimonial-name">Evan Doralt, manager</p>

  <h2 class="abs section-title services-title">Services List</h2>
  <ul class="abs services-list">
    <li><svg class="bullet" viewBox="0 0 18 18"><path d="M8 6 L11 9 L8 12 Z" fill="#9a9a9a"/></svg><span>Luctus et ultriceosue cubil</span></li>
    <li><svg class="bullet" viewBox="0 0 18 18"><path d="M8 6 L11 9 L8 12 Z" fill="#9a9a9a"/></svg><span>Sollicitudin velit sed leelit</span></li>
    <li><svg class="bullet" viewBox="0 0 18 18"><path d="M8 6 L11 9 L8 12 Z" fill="#9a9a9a"/></svg><span>Magna hendrerit samet</span></li>
    <li><svg class="bullet" viewBox="0 0 18 18"><path d="M8 6 L11 9 L8 12 Z" fill="#9a9a9a"/></svg><span>Tincidunt ac viverra sedulec Porta diumet con-</span></li>
    <li><svg class="bullet" viewBox="0 0 18 18"><path d="M8 6 L11 9 L8 12 Z" fill="#9a9a9a"/></svg><span>secteter Adipicisent vestibumole</span></li>
  </ul>
  <div class="abs btn-dark services-btn">READ MORE</div>

  <footer class="abs footer"></footer>
  <div class="abs footer-links">Home | About Us | Services | Investors | FAQ's | Blog | Contact Us</div>
  <div class="abs footer-copy">Larkmoor Insurance&nbsp; (c) 2010&nbsp; |&nbsp; Privacy policy</div>
  <div class="abs social" aria-label="Social links">
    <i style="background:#3b5a98"></i><i style="background:#4fb3df"></i><i style="background:#1f6fa6"></i><i style="background:#e8731f"></i><i style="background:#5a9e3c"></i>
  </div>
</body>
</html>
```